Change consultancy needs business card+ design

We need business card design for a Seattle based consulting firm called
Holloway + Brine. Our firm helps organizations shift their paradigms, lean into change, and reimagine the way they work together.
**Updated**
Our firm name is the logo using black and orange font, see attached. We would like to include the tagline "(Re)imagining how people work"
The final design should find a balance between playful, edgy and professional. For example, we are using the attached goldfish photo on our homepage and like the colors and concept of leaping forward. However, don't want to use the image on the card.
Lastly, depending on the winning design, we will also be looking for stationary/template design that will compliment the business card.
Industry/Entity Type
Business
Font styles to use
Other font styles liked:
- Helvetica
Look and feel
Each slider illustrates characteristics of the customer's brand and the style your logo design should communicate.

```html
<!DOCTYPE html>
<html lang="en">
<head>
<meta charset="utf-8">
<title>Holloway + Brine — Business Card</title>
<link rel="stylesheet" href="https://fonts.googleapis.com/css2?family=Lato:wght@400;700&family=Arimo:wght@400;700&display=swap">
<style>
  :root {
    --page-bg: #d9dcdf;
    --card-top: #f4fafc;
    --card-bottom: #e3f1f6;
    --brand-blue: #29abe2;
    --accent-orange: #f26a21;
    --ink: #111111;
    --ink-soft: #222222;
    --ink-muted: #4a5a63;
  }
  * { box-sizing: border-box; margin: 0; padding: 0; }
  html, body {
    width: 1200px;
    height: 926px;
    overflow: hidden;
    background: var(--page-bg);
  }
  .sheet {
    width: 1200px;
    height: 926px;
    display: flex;
    flex-direction: column;
    align-items: center;
    justify-content: center;
    gap: 48px;
  }
  .card {
    position: relative;
    width: 700px;
    height: 400px;
    background: linear-gradient(180deg, var(--card-top) 0%, var(--card-bottom) 100%);
    box-shadow: 0 6px 20px rgba(0,0,0,0.18);
    overflow: hidden;
  }

  /* Brand name set as type */
  .brand {
    display: flex;
    align-items: center;
    gap: 12px;
    font-family: "Arimo", sans-serif;
    font-weight: 400;
    color: var(--ink);
    line-height: 1;
    white-space: nowrap;
  }
  .brand-square {
    flex: none;
    background: var(--accent-orange);
  }

  /* Front */
  .person {
    position: absolute;
    left: 44px;
    top: 40px;
    font-family: "Lato", sans-serif;
  }
  .person-name {
    font-size: 32px;
    font-weight: 400;
    color: var(--ink);
    letter-spacing: 0.2px;
    line-height: 1;
  }
  .person-name strong { font-weight: 700; }
  .person-title {
    margin-top: 8px;
    font-size: 15px;
    color: var(--accent-orange);
    letter-spacing: 0.8px;
    text-transform: uppercase;
  }
  .contact {
    position: absolute;
    left: 44px;
    top: 196px;
  }
  .contact .brand {
    font-size: 23px;
    margin-bottom: 16px;
  }
  .contact .brand-square { width: 12px; height: 12px; }
  .contact-line {
    display: flex;
    align-items: center;
    gap: 12px;
    font-family: "Lato", sans-serif;
    font-size: 17px;
    color: var(--ink-soft);
    margin-bottom: 8px;
  }
  .contact-line svg { width: 14px; height: 14px; flex: none; }
  .base-band {
    position: absolute;
    left: 0;
    right: 0;
    bottom: 0;
    height: 30px;
    background: var(--brand-blue);
  }

  /* Back */
  .card--back {
    display: flex;
    flex-direction: column;
    align-items: center;
    justify-content: center;
  }
  .card--back .brand { font-size: 40px; gap: 16px; }
  .card--back .brand-square { width: 18px; height: 18px; }
  .tagline {
    margin-top: 18px;
    font-family: "Lato", sans-serif;
    font-size: 18px;
    color: var(--ink-muted);
    letter-spacing: 0.4px;
  }
  .firm-web {
    margin-top: 34px;
    font-family: "Lato", sans-serif;
    font-size: 18px;
    color: var(--accent-orange);
    letter-spacing: 1px;
  }
</style>
</head>
<body>
<main class="sheet">

  <section class="card card--front" aria-label="Business card front">
    <div class="person">
      <p class="person-name">Nora <strong>Whitfield</strong></p>
      <p class="person-title">Managing Partner</p>
    </div>

    <div class="contact">
      <p class="brand"><span class="brand-square"></span>Holloway + Brine, LLC</p>
      <p class="contact-line">
        <svg viewBox="0 0 14 14" aria-hidden="true">
          <path d="M3.2 1.5 L5.2 1.5 L6 4.6 L4.6 5.6 a7 7 0 0 0 3.8 3.8 L9.4 8 L12.5 8.8 L12.5 10.8 a1.8 1.8 0 0 1 -2 1.7 A10 10 0 0 1 1.5 3.5 a1.8 1.8 0 0 1 1.7 -2 Z" fill="var(--accent-orange)"/>
        </svg>
        206.555.0142
      </p>
      <p class="contact-line">
        <svg viewBox="0 0 14 14" aria-hidden="true">
          <g fill="none" stroke="var(--accent-orange)" stroke-width="1.8" stroke-linecap="round">
            <path d="M6 8 L8 6"/>
            <path d="M5 6.5 L3.5 8 a2.1 2.1 0 0 0 3 3 L8 9.5"/>
            <path d="M9 7.5 L10.5 6 a2.1 2.1 0 0 0 -3 -3 L6 4.5"/>
          </g>
        </svg>
        www.hollowaybrine.com
      </p>
    </div>

    <div class="base-band"></div>
  </section>

  <section class="card card--back" aria-label="Business card back">
    <p class="brand"><span class="brand-square"></span>Holloway + Brine, LLC</p>
    <p class="tagline">(Re)imagining how people work</p>
    <p class="firm-web">www.hollowaybrine.com</p>
  </section>

</main>
</body>
</html>
```